Criação de Papelaria Profissional para Computador & Internet
A empresa queria:
" A empresa desenvolve software variados para conectar necessidades de diversos utilizadores por via de internet, para o que procura vender ao que procura comprar, o que procura prestar um serviço ou que precisa de um serviço, bem como facilitar software para Bancos, de modo a deixarem de fazer os trabalhos manuais, cujo slogan é: Conectando Necessidades. "

```html
<!DOCTYPE html>
<html lang="pt-BR">
<head>
<meta charset="utf-8">
<title>Assinatura de e-mail — Korvala Link Net</title>
<link rel="stylesheet" href="https://fonts.googleapis.com/css2?family=Open+Sans:wght@400;600;700&display=swap">
<style>
  :root {
    --backdrop: #e3e3e3;
    --paper: #ffffff;
    --ink: #111111;
    --ink-soft: #333333;
    --icon: #444444;
    --accent: #1c8fd8;
  }
  * { margin: 0; padding: 0; box-sizing: border-box; }
  html, body {
    width: 1200px;
    height: 1200px;
    overflow: hidden;
    background: var(--backdrop);
    font-family: "Open Sans", Arial, sans-serif;
    color: var(--ink);
  }
  .signature {
    position: absolute;
    left: 140px;
    top: 468px;
    width: 924px;
    height: 269px;
    background: var(--paper);
  }
  .brand {
    position: absolute;
    left: 30px;
    top: 0;
    width: 440px;
    height: 269px;
    display: flex;
    align-items: center;
  }
  .brand-row {
    display: flex;
    align-items: center;
    gap: 16px;
  }
  .brand-dot {
    width: 26px;
    height: 26px;
    border-radius: 50%;
    background: var(--accent);
    flex: none;
  }
  .brand-name {
    font-weight: 600;
    font-size: 40px;
    line-height: 1.05;
    color: var(--ink);
    white-space: nowrap;
  }
  .contact {
    position: absolute;
    left: 472px;
    top: 32px;
  }
  .person-name {
    font-weight: 600;
    font-size: 31px;
    line-height: 1.1;
  }
  .person-role {
    font-size: 18px;
    margin-top: 4px;
    color: var(--ink-soft);
  }
  .contact-list {
    list-style: none;
    margin-top: 14px;
  }
  .contact-item {
    display: flex;
    align-items: center;
    gap: 12px;
    margin-bottom: 9px;
  }
  .contact-icon { width: 22px; height: 22px; flex: none; fill: var(--icon); }
  .contact-text {
    font-size: 16px;
    line-height: 20px;
    color: var(--ink-soft);
    white-space: nowrap;
  }
  .contact-text strong { font-weight: 700; color: var(--ink); }
</style>
</head>
<body>
  <section class="signature">
    <div class="brand">
      <div class="brand-row">
        <span class="brand-dot"></span>
        <span class="brand-name">Korvala Link Net</span>
      </div>
    </div>

    <div class="contact">
      <h1 class="person-name">Nome Completo</h1>
      <p class="person-role">CARGO OU FUNÇÃO</p>
      <ul class="contact-list">
        <li class="contact-item">
          <svg class="contact-icon" viewBox="0 0 24 24" aria-hidden="true"><path d="M6.6 10.8a15 15 0 0 0 6.6 6.6l2.2-2.2a1 1 0 0 1 1-.25 11.4 11.4 0 0 0 3.6.57 1 1 0 0 1 1 1V20a1 1 0 0 1-1 1A17 17 0 0 1 3 4a1 1 0 0 1 1-1h3.5a1 1 0 0 1 1 1c0 1.25.2 2.45.57 3.57a1 1 0 0 1-.25 1z"/></svg>
          <span class="contact-text">00 0000.00000<br>00 0000.00000</span>
        </li>
        <li class="contact-item">
          <svg class="contact-icon" viewBox="0 0 24 24" aria-hidden="true"><path d="M12 2a10 10 0 1 0 0 20 10 10 0 0 0 0-20zm6.9 6h-3a15.7 15.7 0 0 0-1.4-3.6A8 8 0 0 1 18.9 8zM12 4c.8 1.2 1.5 2.5 1.9 4h-3.8c.4-1.5 1.1-2.8 1.9-4zM4.3 14a8 8 0 0 1 0-4h3.4a16 16 0 0 0 0 4zm.8 2h3a15.7 15.7 0 0 0 1.4 3.6A8 8 0 0 1 5.1 16zm3-8h-3a8 8 0 0 1 4.4-3.6A15.7 15.7 0 0 0 8.1 8zM12 20c-.8-1.2-1.5-2.5-1.9-4h3.8c-.4 1.5-1.1 2.8-1.9 4zm2.3-6H9.7a14.7 14.7 0 0 1 0-4h4.6a14.7 14.7 0 0 1 0 4zm.2 5.6a15.7 15.7 0 0 0 1.4-3.6h3a8 8 0 0 1-4.4 3.6zm1.8-5.6a16 16 0 0 0 0-4h3.4a8 8 0 0 1 0 4z"/></svg>
          <span class="contact-text">VEREDACONSULTORIA.COM.BR<br><strong>CONTATO</strong>@VEREDACONSULTORIA.COM.BR</span>
        </li>
        <li class="contact-item">
          <svg class="contact-icon" viewBox="0 0 24 24" aria-hidden="true"><path d="M12 2a7 7 0 0 0-7 7c0 5.2 7 13 7 13s7-7.8 7-13a7 7 0 0 0-7-7zm0 9.5A2.5 2.5 0 1 1 12 6.5a2.5 2.5 0 0 1 0 5z"/></svg>
          <span class="contact-text">NOME DA <strong>RUA</strong>, 000 - BAIRRO<br><strong>CIDADE</strong> - ESTADO - <strong>CEP</strong> E PAIS</span>
        </li>
      </ul>
    </div>
  </section>
</body>
</html>
```